Realty Group Needs Classy, Contemporary Letterhead Design

We need a letterhead design for a new realty company located in NY, USA. We buy investment properties to rehabilitate and or keep in our rental portfolio.

```html
<!DOCTYPE html>
<html lang="en">
<head>
<meta charset="utf-8">
<title>Meridian Realty Group – Letterhead</title>
<link href="https://fonts.googleapis.com/css2?family=Open+Sans:wght@400;600;700&display=swap" rel="stylesheet">
<style>
  :root {
    --backdrop: #9a9a9a;
    --paper: #ffffff;
    --brand-purple: #4e2a84;
    --brand-purple-light: #6b4aa3;
    --ink: #2b2b33;
    --ink-soft: #4a4a4a;
    --rule-grey: #b3b3b3;
    --watermark: #f2f2f2;
  }
  * { margin: 0; padding: 0; box-sizing: border-box; }
  html, body {
    width: 1029px; height: 1200px; overflow: hidden;
    background: var(--backdrop);
    font-family: "Open Sans", Arial, sans-serif;
  }
  .letterhead {
    position: absolute; left: 51px; top: 0;
    width: 927px; height: 1200px;
    background: var(--paper);
    overflow: hidden;
  }
  .watermark-area {
    position: absolute; left: 0; top: 700px;
    width: 927px; height: 452px;
    background: linear-gradient(to bottom, rgba(242,242,242,0) 0%, var(--watermark) 35%, var(--watermark) 100%);
  }
  .brand-name {
    position: absolute; left: 63px; top: 90px;
    font-size: 27px; font-weight: 700;
    color: var(--brand-purple);
    letter-spacing: 0.2px;
  }
  .contact-block {
    position: absolute; right: 62px; top: 56px;
    text-align: right;
    font-size: 12.2px; color: var(--ink-soft);
    line-height: 15.5px;
  }
  .contact-block .address { margin-bottom: 5px; }
  .contact-line {
    display: flex; justify-content: flex-end; align-items: center;
    gap: 8px; height: 20.5px;
  }
  .contact-line svg { width: 12px; height: 12px; fill: var(--brand-purple); }
  .letter-date {
    position: absolute; right: 61px; top: 205px;
    font-size: 15px; color: var(--ink-soft);
  }
  .letter-body {
    position: absolute; left: 63px; top: 302px; width: 805px;
    font-size: 15.4px; line-height: 24.3px; color: var(--ink);
  }
  .salutation { margin-bottom: 14px; color: var(--ink-soft); }
  .letter-body p.paragraph { margin-bottom: 24.3px; }
  .sign-off {
    position: absolute; left: 651px; top: 874px;
    font-size: 15.4px; color: var(--ink);
  }
  .footer-rule {
    position: absolute; left: 0; top: 1152px; width: 927px; height: 7px;
    background: var(--rule-grey);
  }
  .footer-band {
    position: absolute; left: 0; top: 1159px; width: 927px; height: 41px;
    background: linear-gradient(to right, var(--brand-purple), var(--brand-purple-light));
    display: flex; align-items: center; justify-content: flex-end;
    padding-right: 62px;
    color: #ffffff; font-size: 17.5px; letter-spacing: 0.3px;
  }
</style>
</head>
<body>
  <main class="letterhead">
    <div class="watermark-area" role="img" aria-label="Faint large brand emblem watermark in light grey"></div>

    <div class="brand-name">Meridian Realty Group, LLC</div>

    <address class="contact-block" style="font-style:normal">
      <div class="address">2750 Linden Park Drive, Suite 200<br>Meridian Realty Group</div>
      <div class="contact-line">(555) 410-2368
        <svg viewBox="0 0 12 12" aria-hidden="true"><path d="M1 4c2-3 8-3 10 0l-1 1.5-2-.6V3.6c-1-.4-3-.4-4 0v1.3l-2 .6z"/><rect x="2.5" y="6.5" width="7" height="4" rx="1"/></svg>
      </div>
      <div class="contact-line">(555) 410-2369
        <svg viewBox="0 0 12 12" aria-hidden="true"><rect x="3" y="1" width="6" height="3"/><rect x="1" y="4.5" width="10" height="4.5" rx="1"/><rect x="3" y="8" width="6" height="3"/></svg>
      </div>
      <div class="contact-line">info@meridianrealtygroup.com
        <svg viewBox="0 0 12 12" aria-hidden="true"><path d="M1 1l10 4-4 1.5L5.5 11z"/></svg>
      </div>
    </address>

    <div class="letter-date">December 29, 2021</div>

    <section class="letter-body">
      <p class="salutation">Dear Customer,</p>
      <p class="paragraph">Lorem ipsum dolor sit amet, consectetur adipiscing elit. Donec orci purus, luctus vitae dignissim eu, iaculis sed purus. Vivamus faucibus, ipsum nec aliquet viverra, leo mauris condimentum ligula, sit amet sagittis enim ligula quis arcu. Nam egestas tortor id nisi porttitor mattis. In tortor ante, ultricies in suscipit a, tempus non massa. Vivamus et auctor mi. Fusce vel massa nulla. Phasellus nec eros mauris, et scelerisque orci.</p>
      <p class="paragraph">Donec malesuada orci vitae nulla accumsan porta a id massa. Quisque accumsan iaculis magna sit amet fringilla. Maecenas consequat, magna eget tincidunt semper, odio nibh rutrum mi, id feugiat ante nisi eu risus. Vestibulum nunc orci, rhoncus a placerat in, ultricies in mi. Cras mattis varius eros, vel fringilla nisi suscipit eget. Quisque scelerisque sagittis nulla at porttitor.</p>
      <p class="paragraph">Sed id augue vitae urna euismod commodo aliquet a quam. Pellentesque arcu velit, cursus et malesuada ut, consequat et diam. Nullam erat sem, rhoncus id ullamcorper vitae, rhoncus et arcu. In ultricies ultricies nulla, ut rutrum nisi iaculis at. Donec eu magna a metus ornare faucibus. Fusce aliquet faucibus ultricies. Morbi semper, est id tincidunt gravida, sem arcu adipiscing lacus, ac bibendum nulla leo eu purus. Quisque nec diam sed risus consectetur a ccumsan quis quis nibh. Vestibulum id purus lorem.</p>
    </section>

    <div class="sign-off">Sincerily,</div>

    <div class="footer-rule"></div>
    <footer class="footer-band">www.meridianrealtygroup.com</footer>
  </main>
</body>
</html>
```